Double-Sided Tri-fold Brochure Needed for PTSD Service Dog Organization that serves US Veterans and

Our current brochure is in desperate need of a face lift. We want something fresh and are open to all ideas. We need our new logo added, we want to change some text around and add more information, and we want to update it with current photos. Text, I imagine, can be changed after winning design is selected. We use our brochure for fundraising, so we'd love to have it easy to read, yet able to make an emotional impact. We need to keep the donation mail-in form already on the old brochure. We are open to artist interpretations, however, for color scheme reference our website is: www.BlueMeadowCanineAllies.com

Target Market(s)

Veterans, First-Responders, Dog Lovers, Donors

Industry/Entity Type

It Service

Requirements
Must have
• Able to elicit an emotional response. We use our brochures for fundraising and information.
Should not have
• anything "cute"

```html
<!DOCTYPE html>
<html lang="en">
<head>
<meta charset="utf-8">
<title>Blue Meadow Canine Allies – Brochure</title>
<link href="https://fonts.googleapis.com/css2?family=Arimo:wght@400;700&display=swap" rel="stylesheet">
<style>
  :root {
    --green: #3f6b3b;
    --green-light: #5a8a4f;
    --paper: #e8e8e8;
    --ink: #3b3b3b;
    --charcoal: #3a3a3c;
    --white: #ffffff;
  }
  * { margin: 0; padding: 0; box-sizing: border-box; }
  html, body { width: 1200px; height: 848px; overflow: hidden; background: var(--paper); }
  .brochure {
    position: relative; width: 1200px; height: 848px; overflow: hidden;
    font-family: "Arimo", Arial, sans-serif; color: var(--ink);
  }
  .shapes { position: absolute; inset: 0; }
  .block { position: absolute; }
  .heading {
    font-weight: 400; font-size: 26px; color: var(--green);
    border-bottom: 2px solid var(--green); padding-bottom: 2px; margin-bottom: 8px;
  }
  .body-text { font-size: 16px; line-height: 20.5px; text-align: justify; }
  .body-text + .body-text { margin-top: 20px; }
  .facts, .benefits { list-style: none; font-size: 16px; line-height: 20.5px; }
  .facts li, .benefits li, .info-list li, .gift-list li {
    position: relative; padding-left: 14px;
  }
  .facts li::before, .benefits li::before, .info-list li::before, .gift-list li::before {
    content: ""; position: absolute; left: 0; top: 6px;
    width: 8px; height: 8px; border: 1.5px solid currentColor; border-radius: 50%; opacity: .7;
  }
  .facts li { margin-bottom: 20px; }
  .middle-panel { color: var(--white); }
  .middle-panel .heading { color: var(--white); border-color: var(--white); font-size: 25px; }
  .benefits li { margin-bottom: 20px; }
  .info-list { list-style: none; font-size: 16px; line-height: 20.5px; text-align: justify; }
  .subhead { color: var(--green-light); font-size: 16px; margin: 14px 0 16px; }
  .gift-list {
    list-style: none; font-size: 16px; line-height: 20.5px;
    display: grid; grid-template-columns: 190px 160px; grid-auto-flow: column; grid-template-rows: repeat(4, auto);
  }
  .tax-note { font-size: 13px; text-align: center; margin-top: 4px; }
  .org-mark { display: flex; align-items: center; gap: 8px; }
  .org-mark .square { width: 14px; height: 14px; background: var(--green); }
  .org-name { font-size: 15px; color: var(--green); line-height: 18px; width: 100px; }
  .contact { font-size: 13.5px; line-height: 17.5px; }
  .contact .web { color: var(--green-light); }
</style>
</head>
<body>
<div class="brochure">
  <svg class="shapes" width="1200" height="848" viewBox="0 0 1200 848">
    <defs>
      <linearGradient id="photoTop" x1="0" y1="0" x2="1" y2="1">
        <stop offset="0" stop-color="#4a3f36"/>
        <stop offset="0.5" stop-color="#9c7a55"/>
        <stop offset="1" stop-color="#6b5a48"/>
      </linearGradient>
      <linearGradient id="photoBottom" x1="0" y1="0" x2="1" y2="0">
        <stop offset="0" stop-color="#6e5a4a"/>
        <stop offset="0.5" stop-color="#c0623a"/>
        <stop offset="1" stop-color="#dcdcdc"/>
      </linearGradient>
    </defs>
    <rect x="403" y="0" width="405" height="848" fill="var(--green)"/>
    <path d="M0,0 H812 Q720,170 520,205 Q300,240 0,120 Z" fill="url(#photoTop)" role="img" aria-label="Photos of veterans greeting their service dogs at an indoor event"/>
    <line x1="403" y1="0" x2="403" y2="215" stroke="var(--white)" stroke-width="4"/>
    <path d="M0,124 Q300,244 520,209 Q720,174 812,0" fill="none" stroke="var(--green)" stroke-width="10"/>
    <path d="M0,134 Q300,252 520,217 Q720,182 818,0" fill="none" stroke="var(--white)" stroke-width="2" opacity=".8"/>
    <ellipse cx="200" cy="900" rx="230" ry="170" fill="var(--charcoal)" stroke="var(--green)" stroke-width="10"/>
    <path d="M580,848 Q640,690 820,650 L1200,640 V848 Z" fill="url(#photoBottom)" role="img" aria-label="Photo of a veteran hugging a supporter at an organization event"/>
    <path d="M572,848 Q632,684 820,642 L1200,632" fill="none" stroke="var(--green)" stroke-width="10"/>
    <line x1="808" y1="0" x2="808" y2="848" stroke="#cfcfcf" stroke-width="1"/>
  </svg>

  <section class="block left-panel" style="left:24px; top:226px; width:368px;">
    <h2 class="heading">Our Mission</h2>
    <p class="body-text">Blue Meadow Canine Allies is committed to providing specialized service dogs to veteran suffering from post-traumatic stress disorder, traumatic brain injury, and / or sexual trauma.</p>
    <p class="body-text">Our mission is to help these men and women regain their lives through the healing power of dogs.</p>
    <h2 class="heading" style="margin-top:18px;">The Reality</h2>
    <ul class="facts">
      <li>22 Veterans commit suicide daily</li>
      <li>5 Active duty soldiers attempt suicide daily (1 Suceeds)</li>
      <li>15% of veterans suffer from PTSD or other major despressive disorders.</li>
      <li>Only 30 to 40% of veterans who screen positive for serious emotional problems, depression, or PTSD seek mental health care.</li>
    </ul>
  </section>

  <section class="block middle-panel" style="left:428px; top:248px; width:366px;">
    <h2 class="heading">How Do Support Dogs Help ?</h2>
    <ul class="benefits">
      <li>Dogs are vigilant. They watch over their soldiers while they sleep, and wake them from nightmares.</li>
      <li>Dogs help relearn trust. They bring a sense of safety soldiers lose on the battlefield.</li>
      <li>Dogs create a barrier in public. Often veterans with PTSD are afraid to leave their homes because they need space.</li>
      <li>Dogs help soldiers relearn how to give affection. War can be a place where love is forgotten and fear takes over.</li>
      <li style="width:356px;">Dog have a vetaran's back-literally. They can be taughr to sweep a room before a veteran enters, to stand at a veteran's back in public so the veteran doesn,t have to worry about sneak attacks.</li>
    </ul>
  </section>

  <section class="block right-panel" style="left:816px; top:22px; width:366px;">
    <ul class="info-list">
      <li>In some instances, veterans withPTSD support dogs are able to decrease their medication. Petting a dog elevates seroton and dopamine-nerve transmitters that produce a calming state.</li>
    </ul>
    <h2 class="heading" style="margin-top:12px;">How Can You Help ?</h2>
    <p class="body-text">On average, it costs between $12,000 and $15,000 to train a PTSD service dog to certification due to the thousands of hours of specialty training involved. Your generous donation allows. Blue Meadow Canine Allies to offer highly trained support dogs at no cost to the veteran.</p>
    <p class="subhead">To help, consider making a</p>
    <ul class="gift-list">
      <li>One-Time Gift</li><li>Monthly Giving</li><li>Planned Giving</li><li>Wills &amp; Bequests</li>
      <li>Corporate Giving</li><li>Matching Gifts</li><li>Gifts of Stock</li><li>Wish List Donation</li>
    </ul>
    <p class="tax-note">All contribution are tax-deductible</p>
    <div class="org-mark" style="margin-top:22px;">
      <span class="square"></span>
      <span class="org-name">Blue Meadow Canine Allies</span>
      <address class="contact" style="font-style:normal; margin-left:6px;">
        450 Harlow Avenue # 120<br>
        Brookfield, IL 60513<br>
        618-555-0142<br>
        <span class="web">www.BlueMeadowCanineAllies.com</span>
      </address>
    </div>
  </section>
</div>
</body>
</html>
```